Web Design Project - Cosmetic Medispa

Our client's current website www.velmoraskin.com.au needs a major overhaul. We need a template for the Home page and an Inner/procedure page.
Their main audience is women 25-55.
The website navigation is as per the attached Word document.
Scrolling animation needed in the header section (we will animate the photo), with the words “Velmora care you can count on” neatly over the top of the image.
The footer of the website needs to contain links to all their procedures per the attached word document (see the bottom part of the document).
“Virtual Consultation” button/icon/banner needed on Home page.
"Velmora Answer Locator" button/icon/banner needed on Home page (this is a tool that lets visitors search for problems (e.g. wrinkles) and it provides a solution (e.g. 'botox').
Add a “Subscribe for Specials” box to all pages.
Colour scheme to be along the lines of that used in the attached Trenzo images.
Home page must use the following images that are attached (flipped yellow bikini, sarong, and doctor).
Industry/Entity Type
Doctor
Look and feel
Each slider illustrates characteristics of the customer's brand and the style your logo design should communicate.

```html
<!DOCTYPE html>
<html lang="en">
<head>
<meta charset="utf-8">
<title>Velmora – Plastic Surgery Perth</title>
<link rel="stylesheet" href="https://fonts.googleapis.com/css2?family=Arimo:wght@400;700&family=Questrial&display=swap">
<style>
:root{
  --orange:#c4570f;
  --orange-deep:#b24c0c;
  --btn-orange:#b8520f;
  --btn-red:#c2330f;
  --nav-top:#3a3a3a;
  --nav-bottom:#141414;
  --page:#2a2a2a;
  --panel:#232323;
  --footer:#2c2c2c;
  --base:#232323;
  --text:#ffffff;
  --muted:#9a9a9a;
}
*{box-sizing:border-box;margin:0;padding:0}
html,body{width:1000px;height:1200px;overflow:hidden;background:var(--page)}
body{font-family:"Arimo",Arial,sans-serif;color:var(--text);position:relative}
.main-nav{position:absolute;left:0;top:0;width:1000px;height:113px;background:linear-gradient(var(--nav-top),var(--nav-bottom));border-bottom:1px solid #000}
.main-nav a{position:absolute;top:0;height:106px;line-height:114px;text-align:left;font-weight:700;font-size:14px;color:var(--orange);text-decoration:none;border-right:1px solid #111}
.main-nav a.current{color:#ececec;border-top:6px solid var(--orange);line-height:102px}
.hero{position:absolute;top:114px;left:0;width:1000px;height:406px}
.brand-panel{position:absolute;left:0;top:0;width:371px;height:406px;background:linear-gradient(135deg,var(--orange-deep),var(--orange));display:flex;align-items:center;justify-content:center;gap:12px}
.brand-panel .mark{width:22px;height:22px;border-radius:50%;background:#fff}
.brand-panel .name{font-family:"Questrial",sans-serif;font-size:30px;letter-spacing:2px;color:#fff}
.hero-photo{position:absolute;left:371px;top:0;width:629px;height:406px;background:linear-gradient(180deg,#4e94db 0%,#6aa9e6 60%,#8c6848 100%)}
.hero-caption{position:absolute;left:371px;top:347px;width:629px;height:59px;background:rgba(40,40,48,.72);font-style:italic;font-weight:700;font-size:18px;line-height:56px;padding-left:15px;color:#fff}
.hero-arrows{position:absolute;right:9px;top:0;font-style:normal;font-size:20px;letter-spacing:10px}
.intro{position:absolute;left:18px;top:530px;width:612px}
.intro h1{font-family:"Questrial",sans-serif;font-weight:400;font-size:19.4px;color:var(--orange);margin-bottom:22px}
.intro p{font-size:12px;line-height:14.5px;margin-bottom:14.5px;width:606px}
.specials{position:absolute;left:690px;top:532px;width:297px;height:313px;background:var(--panel);border-radius:6px}
.specials h2{font-size:14px;font-weight:400;padding:11px 0 0 16px}
.field{position:absolute;left:0;width:297px;font-size:12px}
.field span{position:absolute;left:43px;top:6px}
.field i{position:absolute;left:96px;top:0;width:189px;height:26px;background:#fff}
.submit{position:absolute;left:181px;top:135px;width:100px;height:30px;border-radius:12px;background:var(--btn-red);font-size:12px;text-align:center;line-height:30px}
.specials hr{position:absolute;top:190px;left:0;width:297px;border:0;border-top:1px solid #111}
.cta{position:absolute;left:15px;width:269px;height:30px;border-radius:9px;background:var(--btn-orange);text-align:center;line-height:30px;font-family:"Questrial",sans-serif;font-size:15px}
.site-footer{position:absolute;left:0;top:908px;width:1000px;height:234px;background:var(--footer);border-top:1px solid #1b1b1b}
.link-col{position:absolute;top:18px}
.link-col h3{font-size:14px;font-weight:700;color:var(--orange);margin-bottom:5px}
.link-col li{list-style:none;font-size:12px;color:var(--muted);line-height:24px}
.base-bar{position:absolute;left:0;top:1142px;width:1000px;height:58px;background:var(--base);border-top:1px solid #1a1a1a;font-size:10px}
.legal{position:absolute;left:18px;top:26px}
.social{position:absolute;left:348px;top:19px;display:flex;gap:4px}
.social i{width:22px;height:22px;border-radius:3px;background:#5c7fb8}
.social i:nth-child(3){background:#d9782a}.social i:nth-child(4){background:#b33a2a}
.payments{position:absolute;left:524px;top:23px;display:flex;gap:6px;align-items:center}
.payments i{width:55px;height:16px;background:#e6e6ee;border-radius:2px}
.payments i:nth-child(2){width:28px}
.payments b{width:16px;height:16px;border-radius:50%;background:#e08a20}
.copyright{position:absolute;right:14px;top:25px;font-size:11px;color:var(--orange)}
</style>
</head>
<body>
<nav class="main-nav">
  <a class="current" style="left:0;width:164px;padding-left:77px">Home</a>
  <a style="left:164px;width:151px;padding-left:57px">About</a>
  <a style="left:315px;width:170px;padding-left:50px">Procedures</a>
  <a style="left:485px;width:161px;padding-left:60px">Specials</a>
  <a style="left:646px;width:191px;padding-left:43px">ShopMedia</a>
  <a style="left:837px;width:116px;padding-left:32px;border-right:0">Contact</a>
</nav>

<header class="hero">
  <div class="brand-panel"><span class="mark"></span><span class="name">VELMORA</span></div>
  <div class="hero-photo" role="img" aria-label="Woman with curly hair seen from behind against a clear blue sky"></div>
  <div class="hero-caption">Velmora care you can count on<span class="hero-arrows">‹ ›</span></div>
</header>

<section class="intro">
  <h1>Plastic Surgery Perth - Cosmetic Surgery Perth WA</h1>
  <p>Plastic surgery, cosmetic surgery, dermal fillers, PRP (Dracula therapy or CGF) , neurotox, breast implants, liposuction, wrinkle treatments, IPL, laser hair removal, wrinkle relaxers, facelifts, eyelid surgery, laser surgery and other treatments as shown below are available in Perth, West Perth, Nedlands, Dalkeith, Subiaco, Cottesloe, Swanbourne, Mosman Park, Peppermint Grove, Joondalup, Applecross, Mandurah, Bunbury, Dunsborough, Karratha, Broome, Geraldton and Kalgoorlie.</p>
  <p>Dont go overseas to Thailand or Asia for your cosmetic surgery, risking the the third world problems and the risk of travel after surgery. If you cant drink the water why would you have your surgery there. See latest news for a horror story.</p>
  <p>Save on all your favourite cosmetic treatments. Call the clinic now on 9412 7730 to find out about our October special offers.</p>
  <p>Also ring now on 94186250 for an appointment in our new Applecross Clinic !</p>
  <p>*Not all services offered at all locations. Contact the clinic for more information.</p>
  <p>We aim to provide natural, subtle results from minimally invasive procedures.It is your face and body, only trust the true experts. Full time and only practising in cosmetic plastic surgery. One of the first full time clinics in Australia with international recognition and featuring Dr Hallam who is a Past Cosmetic President.</p>
</section>

<aside class="specials">
  <h2>Subscribe for Specials</h2>
  <div class="field" style="top:41px"><span>Name</span><i></i></div>
  <div class="field" style="top:82px"><span>Email</span><i></i></div>
  <div class="submit">SUBMIT</div>
  <hr>
  <div class="cta" style="top:212px">Virtual Consultation</div>
  <div class="cta" style="top:263px">Velmora Answer Locator</div>
</aside>

<footer class="site-footer">
  <div class="link-col" style="left:19px"><h3>Breast</h3><ul><li>Breast Implants</li><li>Breast Augmentation</li><li>Free Consultation</li></ul></div>
  <div class="link-col" style="left:200px"><h3>Body</h3><ul><li>Liposuction</li><li>Liposculpture</li><li>Liposdissolve</li><li>CryoShape</li><li>Hair Removal</li><li>Fat Transfer</li><li>Mesotherapy</li></ul></div>
  <div class="link-col" style="left:351px"><h3>Face</h3><ul><li>Dermal Fillers</li><li>Wrinkle Relaxers</li><li>Skin Rejuvenation</li><li>Thread Lift</li><li>Chemical Peels</li><li>Laser Resurfacing</li><li>Clear &amp; Bright</li></ul></div>
  <div class="link-col" style="left:522px"><h3>Male</h3><ul><li>Male Breast Reduction</li><li>Dermal Fillers</li><li>Wrinkle Relaxers</li><li>Skin Rolling</li><li>Eyelid Surgery</li><li>Liposculpture</li><li>CryoShape</li></ul></div>
  <div class="link-col" style="left:723px"><h3>About</h3><ul><li>Nedlands Practice</li><li>Applecross Practice</li><li>The Medispa</li><li>Dr Hallam</li><li>Nurse Corinne</li><li>Nursing Staff</li><li>Reception Staff</li></ul></div>
  <div class="link-col" style="left:904px"><h3>Home</h3><ul><li>Specials</li><li>Virtual Consult</li><li>Shop</li><li>Media</li><li>FAQ</li><li>Blog</li><li>Contact Us</li></ul></div>
</footer>

<div class="base-bar">
  <div class="legal">Privacy Policy &nbsp; | &nbsp; Terms &amp; Conditions &nbsp; | &nbsp; Sitemap</div>
  <div class="social"><i></i><i></i><i></i><i></i></div>
  <div class="payments"><i></i><i></i><b></b></div>
  <div class="copyright">© 2012 Velmora Skin Clinic. All Rights Reserved.</div>
</div>
</body>
</html>
```